"Torvela" (spanish restaurant) "Bar de Tapas"

"Torvela" is a spanish restaurant located in the city of Santo Domingo, Dominican Republic. It needs a new and fresh idea for its business card. I would like to take the idea of one of the spaces of the restaurant represented on a business card, for example, the blue and emblematic entrance door of the restaurant, or maybe the bricks on the main room of the restaurant, or how about the bar. Any idea it's good! I invite all the creative designers to participate on the suggestions of it.

What doe sit need? It needs this information on it:

Name: Torvela
Business: Restaurante
Address: Calle Benito Sorel 00, Las Quintas
Phone number: 809-000-0000
website: www.torvelarestaurante.example

Reason: NEED MORE OPTION FOR IT. I WANT YOU TO EXPRESS YOUR DESIGN AS YOU WANT TO NOT AS I ASK YOU TO.

Industry/Entity Type

Restaurant

Contact Information for Business Card

c/Benito Sorel 47

Requirements
Must have
• Creativity. I'm open to new and fresh ideas.
Nice to have
• The entrance door (blue one) would be a plus in the design of the card. Maybe the background could be images of materials like bricks or wood, like the ones in the pictures of the restaurant.

```html
<!DOCTYPE html>
<html lang="es">
<head>
<meta charset="utf-8">
<title>Torvela — Tarjeta de presentación</title>
<link rel="stylesheet" href="https://fonts.googleapis.com/css2?family=Cinzel:wght@400;700&family=Questrial&display=swap">
<style>
  :root {
    --stage: #d9d6d1;
    --card-black: #0b0a09;
    --gold: #c9b48a;
    --ivory: #f3efe6;
    --photo-dark: #2a160b;
    --photo-mid: #6b3d1c;
    --photo-warm: #c08a4a;
    --band: #050505;
  }
  * { margin: 0; padding: 0; box-sizing: border-box; }
  html, body {
    width: 1200px;
    height: 640px;
    overflow: hidden;
    background: var(--stage);
  }
  .stage {
    width: 1200px;
    height: 640px;
    display: flex;
    align-items: center;
    justify-content: center;
    gap: 60px;
  }
  .card {
    width: 520px;
    height: 297px;
    position: relative;
    overflow: hidden;
    box-shadow: 0 10px 28px rgba(0,0,0,.28);
  }

  /* Front */
  .card--front {
    background: var(--card-black);
    display: flex;
    flex-direction: column;
    align-items: center;
    justify-content: center;
    text-align: center;
  }
  .front__tagline {
    font-family: "Cinzel", serif;
    font-weight: 400;
    font-size: 17px;
    letter-spacing: 4px;
    color: var(--gold);
  }
  .front__name {
    font-family: "Cinzel", serif;
    font-weight: 700;
    font-size: 74px;
    line-height: 1;
    letter-spacing: 2px;
    color: var(--gold);
    margin: 6px 0 4px;
  }
  .front__business {
    font-family: "Cinzel", serif;
    font-weight: 400;
    font-size: 30px;
    letter-spacing: 4px;
    color: var(--ivory);
  }

  /* Back */
  .card--back { background: var(--band); }
  .back__photo {
    position: absolute;
    inset: 0 0 54px 0;
    background:
      radial-gradient(ellipse at 62% 38%, rgba(238,190,110,.75) 0%, rgba(192,138,74,.35) 28%, transparent 55%),
      radial-gradient(ellipse at 25% 30%, rgba(160,60,30,.55) 0%, transparent 45%),
      linear-gradient(160deg, var(--photo-mid) 0%, var(--photo-dark) 70%);
  }
  .back__contact {
    position: absolute;
    left: 0; right: 0; bottom: 0;
    height: 54px;
    padding: 0 16px;
    display: flex;
    flex-direction: column;
    justify-content: center;
    align-items: center;
    gap: 3px;
    font-family: "Questrial", sans-serif;
    color: var(--ivory);
  }
  .contact__line { font-size: 12.5px; letter-spacing: .3px; white-space: nowrap; }
  .contact__web { font-size: 12.5px; letter-spacing: 2px; }
</style>
</head>
<body>
  <main class="stage">
    <section class="card card--front" aria-label="Frente de la tarjeta">
      <p class="front__tagline">BAR DE TAPAS</p>
      <h1 class="front__name">TORVELA</h1>
      <p class="front__business">RESTAURANTE</p>
    </section>

    <section class="card card--back" aria-label="Reverso de la tarjeta">
      <div class="back__photo" role="img" aria-label="Fotografía del salón interior del restaurante con paredes de madera y lámparas cálidas"></div>
      <div class="back__contact">
        <p class="contact__line">Torvela Restaurante | Benito Sorel NO. 47 Las Quintas | 809-000-0000</p>
        <p class="contact__web">www.torvelarestaurante.example</p>
      </div>
    </section>
  </main>
</body>
</html>
```